Need UI design for an iOS app game with most of the layout planned

The name of the game is "QUADRIX".

The goal of the game is to find a way to manipulate four numbers so that the end result is 24. Addition, subtraction, multiplication and division may be used and each number can only be used once.

The list of items we need is:

1. launch image, app icon, UI design of all scenes (10-12 scenes) of the app.
2. App background image should support screen size of both 640x1136.
3. Files are preferred to be in (.eps) format so that resolution can be adjusted later. But other file formats are welcome as long as resolution is high enough.
4. Icons, buttons, background image etc. should have their own file so that later they can be moved around in case design is changed.

The detailed requirement is in the attached file. The actual layout can vary if it can help achieve better result. We also attached several screenshots from iOS game "Glimbo". You can use that as your reference.

```html
<!DOCTYPE html>
<html lang="en">
<head>
<meta charset="utf-8">
<title>QUADRIX – Level Select</title>
<link href="https://fonts.googleapis.com/css2?family=Source+Sans+3:wght@400;700&display=swap" rel="stylesheet">
<style>
  :root {
    --bg-top: #0f63c4;
    --bg-mid: #2a8ae0;
    --bg-bottom: #0d4fa8;
    --back-btn: #0a4fb0;
    --back-btn-edge: #06357a;
    --title: #f59a12;
    --label: #0b0b0b;
    --star-gold: #f5a81c;
    --star-edge: #8a5a1a;
    --star-empty: #ffffff;
    --lock: #ffffff;
    --row-1: #ededed;
    --row-2: #c3e6f8;
    --row-3: #9fd7f3;
    --row-4: #3db6e6;
    --row-5: #1d8fe6;
    --row-6: #1877b3;
    --row-7: #1658ab;
    --row-8: #0f3f7c;
  }
  * { margin: 0; padding: 0; box-sizing: border-box; }
  html, body { width: 676px; height: 1200px; overflow: hidden; }
  body {
    position: relative;
    font-family: "Source Sans 3", "Helvetica Neue", Arial, sans-serif;
    background: linear-gradient(180deg, var(--bg-top) 0%, var(--bg-mid) 55%, var(--bg-bottom) 100%);
  }
  .back-button {
    position: absolute;
    left: -6px; top: 6px;
    width: 102px; height: 128px;
    border-radius: 0 64px 64px 0;
    background: radial-gradient(circle at 40% 35%, #2b7de0, var(--back-btn) 70%);
    border: 3px solid var(--back-btn-edge);
    border-left: none;
    top: -2px;
    height: 136px;
    width: 96px;
    border-radius: 0 0 68px 0;
    border-top: none;
    display: flex; align-items: center; justify-content: center;
  }
  .back-button { left: 0; width: 96px; border-radius: 0 68px 68px 0; }
  .back-button svg { width: 56px; height: 56px; margin-right: 8px; }
  .game-title {
    position: absolute;
    left: 0; right: 0; top: 28px;
    text-align: center;
    font-weight: 700;
    font-size: 62px;
    letter-spacing: 1px;
    color: var(--title);
    line-height: 1;
  }
  .level-list { list-style: none; }
  .level-row {
    position: absolute;
    left: 30px;
    width: 612px;
    height: 104px;
    border-radius: 40px;
    border: 2px solid rgba(255,255,255,0.55);
    display: flex; align-items: center; justify-content: space-between;
    padding: 0 34px 0 78px;
  }
  .level-name { font-size: 43px; color: var(--label); font-weight: 400; }
  .level-row--1 { top: 169px; background: var(--row-1); border-color: #fff; }
  .level-row--2 { top: 288px; background: var(--row-2); }
  .level-row--3 { top: 408px; background: var(--row-3); }
  .level-row--4 { top: 534px; background: var(--row-4); }
  .level-row--5 { top: 657px; background: var(--row-5); }
  .level-row--6 { top: 780px; background: var(--row-6); }
  .level-row--7 { top: 902px; background: var(--row-7); }
  .level-row--8 { top: 1024px; background: var(--row-8); }
  .stars { display: flex; gap: 8px; margin-right: -6px; }
  .stars svg { width: 64px; height: 64px; }
  .lock { width: 50px; height: 68px; }
</style>
</head>
<body>
  <div class="back-button" aria-label="Back">
    <svg viewBox="0 0 56 56"><path d="M26 10 L8 28 L26 46 M8 28 H50" fill="none" stroke="#fff" stroke-width="8" stroke-linecap="round" stroke-linejoin="round"/></svg>
  </div>
  <h1 class="game-title">QUADRIX</h1>

  <ul class="level-list">
    <li class="level-row level-row--1">
      <span class="level-name">Level1</span>
      <span class="stars">
        <svg viewBox="0 0 64 64"><polygon points="32,3 40.5,22.5 61,23.5 45,37 50.5,58 32,46.5 13.5,58 19,37 3,23.5 23.5,22.5" fill="var(--star-gold)" stroke="var(--star-edge)" stroke-width="2.5" stroke-linejoin="round"/></svg>
        <svg viewBox="0 0 64 64"><polygon points="32,3 40.5,22.5 61,23.5 45,37 50.5,58 32,46.5 13.5,58 19,37 3,23.5 23.5,22.5" fill="var(--star-empty)" stroke="var(--star-edge)" stroke-width="2.5" stroke-linejoin="round"/></svg>
        <svg viewBox="0 0 64 64"><polygon points="32,3 40.5,22.5 61,23.5 45,37 50.5,58 32,46.5 13.5,58 19,37 3,23.5 23.5,22.5" fill="var(--star-empty)" stroke="var(--star-edge)" stroke-width="2.5" stroke-linejoin="round"/></svg>
      </span>
    </li>
    <li class="level-row level-row--2"><span class="level-name">Level2</span><svg class="lock" viewBox="0 0 50 68"><path d="M11 30 V20 a14 14 0 0 1 28 0 V30" fill="none" stroke="var(--lock)" stroke-width="7"/><rect x="2" y="30" width="46" height="36" rx="3" fill="var(--lock)"/><circle cx="25" cy="44" r="5" fill="var(--row-2)"/><rect x="23" y="45" width="4" height="11" fill="var(--row-2)"/></svg></li>
    <li class="level-row level-row--3"><span class="level-name">Level3</span><svg class="lock" viewBox="0 0 50 68"><path d="M11 30 V20 a14 14 0 0 1 28 0 V30" fill="none" stroke="var(--lock)" stroke-width="7"/><rect x="2" y="30" width="46" height="36" rx="3" fill="var(--lock)"/><circle cx="25" cy="44" r="5" fill="var(--row-3)"/><rect x="23" y="45" width="4" height="11" fill="var(--row-3)"/></svg></li>
    <li class="level-row level-row--4"><span class="level-name">Level4</span><svg class="lock" viewBox="0 0 50 68"><path d="M11 30 V20 a14 14 0 0 1 28 0 V30" fill="none" stroke="var(--lock)" stroke-width="7"/><rect x="2" y="30" width="46" height="36" rx="3" fill="var(--lock)"/><circle cx="25" cy="44" r="5" fill="var(--row-4)"/><rect x="23" y="45" width="4" height="11" fill="var(--row-4)"/></svg></li>
    <li class="level-row level-row--5"><span class="level-name">Level5</span><svg class="lock" viewBox="0 0 50 68"><path d="M11 30 V20 a14 14 0 0 1 28 0 V30" fill="none" stroke="var(--lock)" stroke-width="7"/><rect x="2" y="30" width="46" height="36" rx="3" fill="var(--lock)"/><circle cx="25" cy="44" r="5" fill="var(--row-5)"/><rect x="23" y="45" width="4" height="11" fill="var(--row-5)"/></svg></li>
    <li class="level-row level-row--6"><span class="level-name">Level6</span><svg class="lock" viewBox="0 0 50 68"><path d="M11 30 V20 a14 14 0 0 1 28 0 V30" fill="none" stroke="var(--lock)" stroke-width="7"/><rect x="2" y="30" width="46" height="36" rx="3" fill="var(--lock)"/><circle cx="25" cy="44" r="5" fill="var(--row-6)"/><rect x="23" y="45" width="4" height="11" fill="var(--row-6)"/></svg></li>
    <li class="level-row level-row--7"><span class="level-name">Level7</span><svg class="lock" viewBox="0 0 50 68"><path d="M11 30 V20 a14 14 0 0 1 28 0 V30" fill="none" stroke="var(--lock)" stroke-width="7"/><rect x="2" y="30" width="46" height="36" rx="3" fill="var(--lock)"/><circle cx="25" cy="44" r="5" fill="var(--row-7)"/><rect x="23" y="45" width="4" height="11" fill="var(--row-7)"/></svg></li>
    <li class="level-row level-row--8"><span class="level-name">Level8</span><svg class="lock" viewBox="0 0 50 68"><path d="M11 30 V20 a14 14 0 0 1 28 0 V30" fill="none" stroke="var(--lock)" stroke-width="7"/><rect x="2" y="30" width="46" height="36" rx="3" fill="var(--lock)"/><circle cx="25" cy="44" r="5" fill="var(--row-8)"/><rect x="23" y="45" width="4" height="11" fill="var(--row-8)"/></svg></li>
  </ul>
</body>
</html>
```